Property refurbishment & maintenance Business Card Design

Velkoran Ltd is a leading provider of domestic maintenance, building and refurbishment services. Founded in October 2009 by Milo Velkoran, we aim to provide our customers with exceptional home improvement and maintenance services whilst minimising the disruption and stress caused.
The building services we provide are of the very highest quality. We provide all of your customers with the peace of mind in knowing that they are dealing with experts in construction, renovation and decoration. This is because we are members of the Guild of Certified Tradecrafters (GCT). We have also had our credentials verified by Pledgeline and the UK government's Fair Seal scheme.
Target Market(s)
Private home owners,letting agents,tenants
Industry/Entity Type
Home Improvement
Contact Information for Business Card
Velkoran ltd.
Milo Velkoran
18 Brindle Cope Lane ,Ashcombe Vale,Wrenshire,EN4 2QW,T.01632960517 M:07700900382
E. info@velkoran.co.uk. www.velkoran.co.uk

```html
<!DOCTYPE html>
<html lang="en">
<head>
<meta charset="utf-8">
<title>Velkoran Ltd – Business Card</title>
<link rel="stylesheet" href="https://fonts.googleapis.com/css2?family=Lato:wght@400;700&family=Cinzel:wght@400;600&display=swap">
<style>
  :root {
    --teal: #1f6b5c;
    --gold: #c29a3b;
    --grey: #7a7a7a;
    --ink: #3d3d3d;
    --paper: #ffffff;
    --backdrop: #e9e7e3;
  }
  * { box-sizing: border-box; margin: 0; padding: 0; }
  html, body { width: 1171px; height: 1200px; overflow: hidden; }
  body {
    background: var(--backdrop);
    font-family: "Lato", Arial, sans-serif;
    color: var(--ink);
    position: relative;
  }
  .card {
    position: absolute;
    left: 155px;
    width: 860px;
    height: 490px;
    background: var(--paper);
    border-radius: 4px;
    box-shadow: 0 6px 18px rgba(0,0,0,.12);
    overflow: hidden;
  }
  .card--front { top: 75px; }
  .card--back { top: 635px; }
  .card__bands { position: absolute; inset: 0; width: 860px; height: 490px; }

  .brand {
    position: absolute;
    display: flex;
    align-items: center;
    gap: 16px;
    font-family: "Lato", Arial, sans-serif;
    font-weight: 400;
    color: var(--teal);
    letter-spacing: 6px;
    text-transform: uppercase;
    white-space: nowrap;
  }
  .brand__mark { background: var(--grey); flex: none; }
  .card--front .brand { left: 150px; top: 190px; font-size: 62px; }
  .card--front .brand__mark { width: 22px; height: 22px; }
  .card--back .brand { left: 60px; top: 210px; font-size: 40px; letter-spacing: 4px; }
  .card--back .brand__mark { width: 16px; height: 16px; }

  .website {
    position: absolute;
    right: 80px;
    bottom: 70px;
    font-size: 20px;
    letter-spacing: 3px;
    color: var(--teal);
    font-weight: 700;
  }

  .person {
    position: absolute;
    right: 70px;
    top: 48px;
    font-family: "Cinzel", Georgia, serif;
    font-weight: 600;
    font-size: 32px;
    letter-spacing: 2px;
    color: var(--teal);
    white-space: nowrap;
  }
  .services {
    position: absolute;
    right: 70px;
    top: 110px;
    text-align: right;
  }
  .services__title {
    display: inline-block;
    background: var(--gold);
    color: var(--paper);
    font-weight: 700;
    font-size: 15px;
    letter-spacing: 1px;
    text-transform: uppercase;
    padding: 6px 18px;
    border-radius: 16px;
    margin-bottom: 10px;
  }
  .services__list { list-style: none; }
  .services__item {
    font-size: 18px;
    line-height: 29px;
    color: var(--ink);
    white-space: nowrap;
  }
  .services__item::after {
    content: "";
    display: inline-block;
    width: 7px; height: 7px;
    border-radius: 50%;
    background: var(--ink);
    margin-left: 10px;
    vertical-align: middle;
  }

  .contact {
    position: absolute;
    left: 60px;
    bottom: 40px;
    display: flex;
    gap: 18px;
    align-items: stretch;
  }
  .contact__icons {
    background: var(--teal);
    border-radius: 10px;
    padding: 12px 10px;
    display: flex;
    flex-direction: column;
    justify-content: space-between;
    gap: 10px;
  }
  .contact__icons svg { width: 22px; height: 22px; display: block; }
  .contact__lines { list-style: none; font-size: 18px; line-height: 30px; color: var(--ink); white-space: nowrap; }
</style>
</head>
<body>

<section class="card card--front" aria-label="Business card front">
  <svg class="card__bands" viewBox="0 0 860 490" aria-hidden="true">
    <path fill="var(--gold)" d="M842 0 H860 V300 H842 Z"/>
    <path fill="var(--teal)" d="M420 490 V478 Q420 466 432 466 H820 Q842 466 842 444 V300 H860 V490 Z"/>
  </svg>
  <div class="brand"><span class="brand__mark"></span>Velkoran</div>
  <p class="website">www.velkoran.co.uk</p>
</section>

<section class="card card--back" aria-label="Business card back">
  <svg class="card__bands" viewBox="0 0 860 490" aria-hidden="true">
    <path fill="var(--gold)" d="M842 0 H860 V300 H842 Z"/>
    <path fill="var(--teal)" d="M420 490 V478 Q420 466 432 466 H820 Q842 466 842 444 V300 H860 V490 Z"/>
  </svg>

  <h1 class="person">MILO VELKORAN</h1>

  <div class="services">
    <h2 class="services__title">Our Services</h2>
    <ul class="services__list">
      <li class="services__item">Maintenance</li>
      <li class="services__item">Domestic Building</li>
      <li class="services__item">Decorating Specialists</li>
      <li class="services__item">Home Refurbishments</li>
      <li class="services__item">Kitchens and Bathrooms</li>
      <li class="services__item">Electrics, Plumbing &amp; Heating</li>
    </ul>
  </div>

  <div class="brand"><span class="brand__mark"></span>Velkoran</div>

  <div class="contact">
    <div class="contact__icons" aria-hidden="true">
      <svg viewBox="0 0 24 24"><rect x="7" y="2" width="10" height="20" rx="2" fill="none" stroke="#fff" stroke-width="2"/><circle cx="12" cy="18" r="1.2" fill="#fff"/></svg>
      <svg viewBox="0 0 24 24"><path fill="#fff" d="M6 3 L10 3 L11 8 L8.5 9.5 Q10.5 13.5 14.5 15.5 L16 13 L21 14 L21 18 Q21 21 18 21 Q4 20 3 6 Q3 3 6 3 Z"/></svg>
      <svg viewBox="0 0 24 24"><rect x="2" y="5" width="20" height="14" rx="1.5" fill="none" stroke="#fff" stroke-width="2"/><path d="M3 6 L12 13 L21 6" fill="none" stroke="#fff" stroke-width="2"/></svg>
      <svg viewBox="0 0 24 24"><path fill="#fff" d="M12 2 C7.6 2 5 5.2 5 9 C5 14 12 22 12 22 C12 22 19 14 19 9 C19 5.2 16.4 2 12 2 Z"/><circle cx="12" cy="9" r="2.6" fill="var(--teal)"/></svg>
    </div>
    <ul class="contact__lines">
      <li>07700900382</li>
      <li>01632960517</li>
      <li>info@velkoran.co.uk</li>
      <li>18 Brindle Cope Lane ,</li>
      <li>Ashcombe Vale,Wrenshire,EN4 2QW</li>
    </ul>
  </div>
</section>

</body>
</html>
```